Meridian Heritage Hall Vancouver the tournament promotion

We are hosting every game for the the tournament at our banquet hall.
we want to drive traffic to our website www.meridianhallevents.example
we cannot use the word the tournament, or any of the other registered trademarks or brands associated. Rovo, kellmarsh, etc.
Our pricing includes coffee and breakfast or lunch
Beer on Sale at 9am each day.
We are showing every day of the the tournament, starting early in the morning.

Target Market(s)

Soccer fans of all stripes

Industry/Entity Type

hospitality

Requirements
Must have
• bold images, could be black and white but very high contrast. we need a square for instagram, for a button for our ticket purchase agent as well as a poster for the internet, for our website and our ticket promoters.
Nice to have
• promote the website
Should not have
• brands, logos other than the meridian hall

```html
<!DOCTYPE html>
<html lang="en">
<head>
<meta charset="utf-8">
<title>Meridian Heritage Hall – Tournament Screenings</title>
<link href="https://fonts.googleapis.com/css2?family=Montserrat:wght@300;400;500;600;700;800&display=swap" rel="stylesheet">
<style>
  :root {
    --night: #0d0a12;
    --night-mid: #1a1224;
    --water: #120c2a;
    --white: #ffffff;
    --button-top: #8a45e6;
    --button-bottom: #5d22b8;
    --button-edge: #b78cff;
    --shadow: rgba(0,0,0,0.75);
  }
  * { margin: 0; padding: 0; box-sizing: border-box; }
  html, body { width: 1200px; height: 1200px; overflow: hidden; background: var(--night); }
  .poster {
    position: relative; width: 1200px; height: 1200px; overflow: hidden;
    background: linear-gradient(180deg, var(--night) 0%, var(--night-mid) 40%, var(--night) 100%);
    font-family: "Montserrat", sans-serif; color: var(--white);
  }
  .skyline-photo {
    position: absolute; left: 0; top: 420px; width: 1200px; height: 780px;
    background:
      radial-gradient(ellipse 260px 320px at 70px 330px, rgba(50,60,220,0.75), transparent 70%),
      radial-gradient(ellipse 220px 300px at 560px 330px, rgba(60,70,220,0.55), transparent 70%),
      radial-gradient(ellipse 200px 260px at 680px 360px, rgba(200,50,210,0.6), transparent 70%),
      radial-gradient(ellipse 180px 260px at 380px 380px, rgba(220,120,60,0.35), transparent 70%),
      radial-gradient(ellipse 260px 260px at 1080px 350px, rgba(70,70,200,0.45), transparent 70%),
      linear-gradient(180deg, transparent 0%, rgba(40,30,90,0.55) 30%, rgba(60,30,120,0.6) 62%, var(--water) 70%, #1b1240 85%, var(--water) 100%);
  }
  .hero-row { position: absolute; inset: 0; }
  .orb { position: absolute; border-radius: 50%; }
  .orb-earth {
    left: 58px; top: 125px; width: 320px; height: 320px;
    background: radial-gradient(circle at 45% 40%, #e8edf2 0%, #7d93ad 35%, #2c4670 70%, #0f1f3c 100%);
  }
  .orb-coffee {
    left: 436px; top: 125px; width: 316px; height: 316px;
    background: radial-gradient(circle at 50% 50%, #2a0c06 0%, #3a1408 19%, #f4f4f4 21%, #e6e6e6 33%, #f7f7f7 45%, #cfcfcf 100%);
  }
  .orb-ball {
    left: 820px; top: 125px; width: 316px; height: 316px;
    background: radial-gradient(circle at 45% 40%, #ffffff 0%, #f2eeee 40%, #e98a5a 70%, #4f8fd8 88%, #d9d9e6 100%);
  }
  .plus { position: absolute; width: 92px; height: 92px; }
  .plus-one { left: 365px; top: 238px; }
  .plus-two { left: 750px; top: 238px; }
  .site-url {
    position: absolute; left: 0; width: 1200px; top: 492px; text-align: center;
    font-size: 60px; font-weight: 700; letter-spacing: -0.5px;
    text-shadow: 0 3px 8px var(--shadow);
  }
  .beer-headline {
    position: absolute; left: 0; width: 1200px; top: 693px; text-align: center;
    font-size: 57px; font-weight: 600; line-height: 56px;
    text-shadow: 0 2px 6px var(--shadow);
  }
  .schedule-copy {
    position: absolute; left: 0; width: 1200px; top: 820px; text-align: center;
    font-size: 43px; font-weight: 400; line-height: 41px;
    text-shadow: 0 2px 6px var(--shadow);
  }
  .ticket-button {
    position: absolute; left: 338px; top: 987px; width: 526px; height: 84px;
    border-radius: 16px; border: 2px solid var(--button-edge);
    background: linear-gradient(180deg, var(--button-top), var(--button-bottom));
    box-shadow: 0 4px 12px rgba(0,0,0,0.5);
    display: flex; align-items: center; justify-content: center;
    font-size: 57px; font-weight: 600; text-shadow: 0 2px 4px rgba(0,0,0,0.5);
  }
  .pricing-note {
    position: absolute; left: 0; width: 1200px; top: 1102px; text-align: center;
    font-size: 39px; font-weight: 400; letter-spacing: 0.3px;
    text-shadow: 0 2px 6px var(--shadow);
  }
</style>
</head>
<body>
  <main class="poster">
    <div class="skyline-photo" role="img" aria-label="Night city skyline lit in blue and purple, reflected in the water"></div>

    <section class="hero-row">
      <div class="orb orb-earth" role="img" aria-label="Photo of planet Earth from space"></div>
      <div class="orb orb-coffee" role="img" aria-label="Top view of a cup of black coffee on a white saucer"></div>
      <div class="orb orb-ball" role="img" aria-label="White soccer ball with colourful streak pattern"></div>
      <svg class="plus plus-one" viewBox="0 0 90 90" aria-hidden="true">
        <rect x="31" y="0" width="28" height="90" fill="#ffffff"/>
        <rect x="0" y="31" width="90" height="28" fill="#ffffff"/>
      </svg>
      <svg class="plus plus-two" viewBox="0 0 90 90" aria-hidden="true">
        <rect x="31" y="0" width="28" height="90" fill="#ffffff"/>
        <rect x="0" y="31" width="90" height="28" fill="#ffffff"/>
      </svg>
    </section>

    <h1 class="site-url">www.meridianhallevents.example</h1>

    <p class="beer-headline">Beer on Sale<br>at 9am each day</p>

    <p class="schedule-copy">We are showing every day,<br>of the tournament,<br>starting early in the morning.</p>

    <div class="ticket-button">Tickets on Sale</div>

    <p class="pricing-note">Our pricing includes coffee and breakfast or lunch</p>
  </main>
</body>
</html>
```